Profesional personal website needs design and business card

I need a business card with my professional name as a logo "Marlo Vitality" for my business. I am a Wellness Coach, consultant and trainer. So it should be professional, wellness oriented and modern.

Target Market(s)

Private clients, governments, corporations. Luxury and high market.

Industry/Entity Type

Health And Wellness

Contact Information for Business Card

Marlo Vitality should be the logo

Colors

Designer to choose colors to be used in the design.

Requirements
Must have
• Marlo Vitality
• Name: Tomás Arribal
• Wellness Coach, Consultant & Trainer.
• Website: www.marlovitality.example
• Phone:
• Spain (+34) 612 480 397
• (USA) +1 (555) 318 2046
Nice to have
• The most important is the design of "Marlo Vitality", as this is going to be my personal brand logo. It should be professional, wellness, high end and actual.
Should not have
• no golds, no baroque style..

```html
<!DOCTYPE html>
<html lang="en">
<head>
<meta charset="utf-8">
<title>Marlo Vitality – Business Card</title>
<link href="https://fonts.googleapis.com/css2?family=Roboto:wght@400;700&display=swap" rel="stylesheet">
<style>
  :root {
    --page-bg: #e4e2df;
    --card-top: #f4f6f8;
    --card-bottom: #e6ecf1;
    --brand-blue: #1a4f9c;
    --band-light: #b9cfe0;
    --band-green: #5f9a4c;
    --band-blue: #1656a3;
    --text-grey: #3a3d42;
    --icon-blue: #1f5fae;
  }
  * { margin: 0; padding: 0; box-sizing: border-box; }
  html, body {
    width: 1200px; height: 970px; overflow: hidden;
    background: var(--page-bg);
    font-family: "Roboto", Arial, sans-serif;
  }
  .card {
    position: absolute;
    left: 60px; top: 179px;
    width: 1080px; height: 612px;
    border-radius: 30px;
    overflow: hidden;
    background: linear-gradient(160deg, var(--card-top) 0%, var(--card-bottom) 100%);
    box-shadow: 0 14px 40px rgba(0,0,0,0.18);
  }
  .wave-band {
    position: absolute; left: 0; bottom: 0;
    width: 100%; height: 190px;
    background: linear-gradient(to bottom, var(--card-bottom) 0%, var(--band-light) 25%, var(--band-green) 45%, var(--band-blue) 80%);
  }
  .brand {
    position: absolute; left: 78px; top: 120px;
    display: flex; align-items: center; gap: 18px;
  }
  .brand-dot {
    width: 46px; height: 46px; border-radius: 50%;
    background: var(--brand-blue);
  }
  .brand-name {
    font-size: 50px; font-weight: 400; color: var(--brand-blue);
    letter-spacing: 0.5px;
  }
  .identity {
    position: absolute; right: 57px; top: 108px; text-align: right;
  }
  .person-name {
    font-size: 33px; font-weight: 700; color: var(--brand-blue);
  }
  .person-role {
    margin-top: 8px; font-size: 23px; color: var(--text-grey);
  }
  .contacts {
    position: absolute; right: 55px; top: 250px;
    list-style: none; text-align: right;
  }
  .contact {
    display: flex; align-items: center; justify-content: flex-end;
    gap: 12px; height: 41px;
    font-size: 24px; color: var(--text-grey);
  }
  .contact-icon { width: 36px; height: 36px; flex: none; }
</style>
</head>
<body>
  <article class="card">
    <div class="wave-band" role="img" aria-label="Decorative green, pink and blue wave band along the bottom of the card"></div>

    <div class="brand">
      <span class="brand-dot"></span>
      <span class="brand-name">Marlo Vitality</span>
    </div>

    <header class="identity">
      <h1 class="person-name">Tomás Arribal</h1>
      <p class="person-role">Coach, Consultant &amp; Trainer.</p>
    </header>

    <ul class="contacts">
      <li class="contact">
        <span>Spain (+34) 612 480 397</span>
        <svg class="contact-icon" viewBox="0 0 36 36" aria-hidden="true">
          <circle cx="18" cy="18" r="17" fill="var(--icon-blue)"/>
          <circle cx="18" cy="18" r="13" fill="none" stroke="#fff" stroke-width="1.5"/>
          <path d="M13 11 l3 -1 2 5 -2 1.5 c1 2.5 2.5 4 4.5 5 l1.5 -2 5 2 -1 3 c-7 1 -14 -6 -13 -13.5z" fill="#fff"/>
        </svg>
      </li>
      <li class="contact">
        <span>(USA) +1 (555) 318 2046</span>
        <svg class="contact-icon" viewBox="0 0 36 36" aria-hidden="true">
          <circle cx="18" cy="18" r="17" fill="var(--icon-blue)"/>
          <circle cx="18" cy="18" r="13" fill="none" stroke="#fff" stroke-width="1.5"/>
          <path d="M13 11 l3 -1 2 5 -2 1.5 c1 2.5 2.5 4 4.5 5 l1.5 -2 5 2 -1 3 c-7 1 -14 -6 -13 -13.5z" fill="#fff"/>
        </svg>
      </li>
      <li class="contact">
        <span>www.marlovitality.example</span>
        <svg class="contact-icon" viewBox="0 0 36 36" aria-hidden="true">
          <circle cx="18" cy="18" r="17" fill="var(--icon-blue)"/>
          <g fill="none" stroke="#fff" stroke-width="1.4">
            <circle cx="18" cy="18" r="9"/>
            <ellipse cx="18" cy="18" rx="4" ry="9"/>
            <line x1="9" y1="18" x2="27" y2="18"/>
            <line x1="10.5" y1="13.5" x2="25.5" y2="13.5"/>
            <line x1="10.5" y1="22.5" x2="25.5" y2="22.5"/>
          </g>
        </svg>
      </li>
    </ul>
  </article>
</body>
</html>
```